Larkspur Ridge Management - Business Cards

I need business cards. My current logo was designed by a designer at this site and I very much like and am happy with the results. I would like a business card that is trendy, unique, current yet professional. I deal with high net worth clients daily

Target Market(s)

Out of state investors looking to get into the rental market in Ohio

Industry/Entity Type

Property Management, Consulting

Contact Information for Business Card

Name, Title (Chief Financial Officer) office phone number (555) 817-3094 website address larkridgemgmt.example

Font styles to use
Sans Serif

Colors
0054AA
0677BA
7BADD7
CADEEF
E8F1F8
0094D4
00A9DD
6FCCEA
C7EBF8
E9F6FB
00AB8E
00BBA5
67D7C9
C6EFE9
E9F9F6

```html
<!DOCTYPE html>
<html lang="en">
<head>
<meta charset="utf-8">
<title>Larkspur Ridge Management – Business Cards</title>
<link rel="stylesheet" href="https://fonts.googleapis.com/css2?family=Lexend:wght@300;400;500;600&display=swap">
<style>
  :root {
    --board: #cccccc;
    --navy: #22355a;
    --red: #d32f3a;
    --white: #ffffff;
  }
  * { margin: 0; padding: 0; box-sizing: border-box; }
  html, body { width: 1200px; height: 1200px; overflow: hidden; }
  body { background: var(--board); font-family: "Lexend", sans-serif; color: var(--navy); position: relative; }

  .card { position: absolute; width: 520px; height: 296px; background: var(--white); overflow: hidden; }
  .card--front-stripes { left: 63px; top: 287px; }
  .card--back-compact { left: 630px; top: 287px; }
  .card--front-navy { left: 63px; top: 670px; background: var(--navy); }
  .card--back-wide { left: 630px; top: 670px; }

  .wordmark { position: absolute; text-align: center; font-weight: 600; line-height: 1.15; color: var(--navy); transform: translate(-50%, -50%); white-space: nowrap; }
  .wordmark--light { color: var(--white); }

  .stripe { position: absolute; background: var(--navy); }

  .site-line { position: absolute; right: 32px; font-weight: 300; font-size: 12px; letter-spacing: .3px; color: var(--navy); }

  .accent-bar { position: absolute; left: 0; top: 125px; width: 9px; height: 45px; background: var(--red); }
  .person-name { position: absolute; font-weight: 500; letter-spacing: 2.5px; color: var(--navy); }
  .person-title { position: absolute; font-weight: 500; color: var(--navy); }
  .divider { position: absolute; height: 1.5px; background: var(--navy); }
  .footer-band { position: absolute; left: 0; bottom: 0; width: 100%; height: 8px; background: var(--navy); }
  .red-rule { position: absolute; left: 0; width: 100%; height: 2px; background: var(--red); }

  .contact { position: absolute; display: flex; align-items: center; font-weight: 300; color: var(--navy); white-space: nowrap; }
  .contact svg { flex: none; }
  .contact--sm { font-size: 12px; gap: 9px; }
  .contact--lg { font-size: 16px; gap: 13px; letter-spacing: .3px; }
  .contact .phone-digits { letter-spacing: 1.5px; }
  .address-right { position: absolute; right: 47px; font-weight: 300; font-size: 11px; }
</style>
</head>
<body>

<svg width="0" height="0" style="position:absolute">
  <defs>
    <g id="icon-phone"><circle cx="12" cy="12" r="12" fill="#d32f3a"/><path d="M8 6.5l2 2.2-1.2 1.5c.8 1.8 2.2 3.2 4 4l1.5-1.2 2.2 2-1.3 1.8c-4 -.6-7.4-4-8-8z" fill="#fff"/></g>
    <g id="icon-globe"><circle cx="12" cy="12" r="12" fill="#d32f3a"/><g fill="none" stroke="#fff" stroke-width="1.2"><circle cx="12" cy="12" r="6"/><ellipse cx="12" cy="12" rx="2.6" ry="6"/><path d="M6 12h12M7 9h10M7 15h10"/></g></g>
    <g id="icon-mail"><circle cx="12" cy="12" r="12" fill="#d32f3a"/><rect x="6.5" y="8" width="11" height="8" fill="#fff"/><path d="M6.5 8l5.5 4.5L17.5 8M6.5 16l4-3.5M17.5 16l-4-3.5" fill="none" stroke="#d32f3a" stroke-width="1"/></g>
    <g id="icon-pin"><circle cx="12" cy="12" r="12" fill="#d32f3a"/><path d="M12 19s-5-5.2-5-8.6a5 5 0 0 1 10 0C17 13.8 12 19 12 19z" fill="#fff"/><circle cx="12" cy="10.5" r="1.9" fill="#d32f3a"/></g>
  </defs>
</svg>

<!-- Front: horizontal stripes -->
<section class="card card--front-stripes">
  <div class="stripe" style="left:0;top:142px;width:176px;height:2px"></div>
  <div class="stripe" style="left:0;top:147px;width:176px;height:21px"></div>
  <div class="stripe" style="left:0;top:170px;width:176px;height:2px"></div>
  <div class="stripe" style="left:342px;top:142px;width:178px;height:2px"></div>
  <div class="stripe" style="left:342px;top:147px;width:178px;height:21px"></div>
  <div class="stripe" style="left:342px;top:170px;width:178px;height:2px"></div>
  <div class="wordmark" style="left:259px;top:156px;font-size:19px">Larkspur Ridge<br>Management</div>
  <p class="site-line" style="top:262px">www.yourwebsite.com</p>
</section>

<!-- Back: compact contact layout -->
<section class="card card--back-compact">
  <div class="wordmark" style="left:412px;top:89px;font-size:14px">Larkspur Ridge<br>Management</div>
  <div class="accent-bar"></div>
  <h2 class="person-name" style="left:46px;top:126px;font-size:22px">Your Name</h2>
  <p class="person-title" style="left:46px;top:151px;font-size:13px">Your Title</p>
  <div class="divider" style="left:46px;top:180px;width:427px"></div>
  <p class="contact contact--sm" style="left:46px;top:195px"><svg width="16" height="16" viewBox="0 0 24 24"><use href="#icon-phone"/></svg><span class="phone-digits">123-456-789</span></p>
  <p class="contact contact--sm" style="left:46px;top:215px"><svg width="16" height="16" viewBox="0 0 24 24"><use href="#icon-globe"/></svg>www.yourwebsite.com</p>
  <p class="contact contact--sm" style="left:46px;top:236px"><svg width="16" height="16" viewBox="0 0 24 24"><use href="#icon-mail"/></svg>email@info.com</p>
  <p class="address-right" style="top:236px">Your Address and Country</p>
  <div class="footer-band"></div>
</section>

<!-- Front: navy -->
<section class="card card--front-navy">
  <div class="wordmark wordmark--light" style="left:259px;top:148px;font-size:24px">Larkspur Ridge<br>Management</div>
  <div class="red-rule" style="top:256px"></div>
  <p class="site-line" style="top:264px;right:27px;font-size:14px;color:var(--white)">www.yourwebsite.com</p>
</section>

<!-- Back: wide contact layout -->
<section class="card card--back-wide">
  <div class="wordmark" style="left:122px;top:148px;font-size:19px">Larkspur Ridge<br>Management</div>
  <h2 class="person-name" style="left:259px;top:58px;font-size:25px">Your Name</h2>
  <p class="person-title" style="left:259px;top:89px;font-size:15px">Your Title</p>
  <p class="contact contact--lg" style="left:259px;top:124px"><svg width="22" height="22" viewBox="0 0 24 24"><use href="#icon-phone"/></svg><span class="phone-digits">123-456-789</span></p>
  <p class="contact contact--lg" style="left:259px;top:153px"><svg width="22" height="22" viewBox="0 0 24 24"><use href="#icon-globe"/></svg>www.yourwebsite.com</p>
  <p class="contact contact--lg" style="left:259px;top:181px"><svg width="22" height="22" viewBox="0 0 24 24"><use href="#icon-mail"/></svg>email@info.com</p>
  <p class="contact contact--lg" style="left:259px;top:208px"><svg width="22" height="22" viewBox="0 0 24 24"><use href="#icon-pin"/></svg>Your Address and Country</p>
  <div class="red-rule" style="top:257px"></div>
</section>

</body>
</html>
```